Modern Business Card For A Digital Advertising Company

I'll be print on the Tarn Prints Velour paper http://us.tarnprints.example/products/velour/business-cards.html
Need's to be modern and use the color palette of the logo or gray scales. I think integrating the pixelation of the logo in to the card and having it wrap from one side to the other could be interesting. My company provides ad operations, web development, and number of other services to websites around the world. You can see my website at http://www.pixelharbor.example
Contact info on the card needs to have
Dana Welloby
President
p.555.318.4406
dana@pixelharbor.example
http://www.pixelharbor.example
Doesn't necessarily need to be in that order
Target Market(s)
Website owners
Industry/Entity Type
Business
Look and feel

```html
<!DOCTYPE html>
<html lang="en">
<head>
<meta charset="utf-8">
<title>Pixel Harbor Business Card</title>
<link rel="stylesheet" href="https://fonts.googleapis.com/css2?family=Ubuntu:wght@400;500;700&display=swap">
<style>
  :root {
    --brand-green: #8dc43f;
    --brand-green-dark: #7cb233;
    --ink: #2f2f31;
    --ink-soft: #5a5a5c;
    --paper: #ffffff;
    --backdrop: #e4e4e4;
  }
  html, body {
    margin: 0;
    padding: 0;
    width: 1200px;
    height: 861px;
    overflow: hidden;
    background: var(--backdrop);
    font-family: "Ubuntu", sans-serif;
  }
  .stage {
    position: relative;
    width: 1200px;
    height: 861px;
  }
  .card {
    position: absolute;
    top: 285px;
    width: 500px;
    height: 286px;
    box-shadow: 0 6px 18px rgba(0,0,0,0.18);
    overflow: hidden;
  }
  .card--front {
    left: 70px;
    background: var(--brand-green);
    display: flex;
    align-items: center;
    justify-content: center;
  }
  .card--back {
    left: 630px;
    background: var(--paper);
  }
  .front-wordmark {
    display: flex;
    align-items: center;
    gap: 16px;
    color: var(--paper);
    font-weight: 700;
    font-size: 46px;
    letter-spacing: 1px;
  }
  .front-wordmark .mark-square {
    width: 40px;
    height: 40px;
    background: var(--paper);
  }
  .back-wordmark {
    position: absolute;
    left: 28px;
    top: 46px;
    display: flex;
    align-items: center;
    gap: 7px;
    color: var(--brand-green);
    font-weight: 700;
    font-size: 16px;
    line-height: 1;
  }
  .back-wordmark .mark-square {
    width: 14px;
    height: 14px;
    background: var(--brand-green);
  }
  .pixel-band {
    position: absolute;
    left: 132px;
    top: 32px;
    right: 0;
    height: 78px;
    background: linear-gradient(90deg, rgba(141,196,63,0.35), var(--brand-green) 70%);
  }
  .person {
    position: absolute;
    right: 44px;
    top: 136px;
    text-align: right;
  }
  .person-name {
    margin: 0;
    color: var(--ink);
    font-weight: 500;
    font-size: 21px;
    letter-spacing: 0.3px;
  }
  .person-title {
    margin: 3px 0 0;
    color: var(--ink-soft);
    font-weight: 500;
    font-size: 11px;
    letter-spacing: 0.5px;
  }
  .contact-list {
    position: absolute;
    right: 44px;
    top: 198px;
    margin: 0;
    padding: 0;
    list-style: none;
  }
  .contact-item {
    display: flex;
    align-items: center;
    justify-content: flex-end;
    gap: 7px;
    height: 21px;
    color: var(--ink-soft);
    font-size: 11.5px;
  }
  .contact-icon {
    width: 14px;
    height: 14px;
    background: var(--brand-green);
    display: block;
  }
</style>
</head>
<body>
<main class="stage">
  <section class="card card--front" aria-label="Card front">
    <div class="front-wordmark">
      <span class="mark-square"></span>
      <span>Pixel Harbor</span>
    </div>
  </section>

  <section class="card card--back" aria-label="Card back">
    <div class="back-wordmark">
      <span class="mark-square"></span>
      <span>Pixel Harbor</span>
    </div>
    <div class="pixel-band" role="img" aria-label="Band of green pixel squares fading in from the left"></div>

    <div class="person">
      <p class="person-name">DANA WELLOBY</p>
      <p class="person-title">PRESIDENT</p>
    </div>

    <ul class="contact-list">
      <li class="contact-item">
        <span>555.318.4406</span>
        <svg class="contact-icon" viewBox="0 0 14 14" aria-hidden="true">
          <rect width="14" height="14" fill="var(--brand-green)"/>
          <path d="M4 10.5 L9.5 5" stroke="#fff" stroke-width="2" stroke-linecap="round"/>
          <rect x="8.5" y="3" width="2.5" height="2.5" fill="#fff"/>
        </svg>
      </li>
      <li class="contact-item">
        <span>dana@pixelharbor.example</span>
        <svg class="contact-icon" viewBox="0 0 14 14" aria-hidden="true">
          <rect width="14" height="14" fill="var(--brand-green)"/>
          <rect x="3" y="4.5" width="8" height="5.5" fill="none" stroke="#fff" stroke-width="1"/>
          <path d="M3 4.5 L7 7.5 L11 4.5" fill="none" stroke="#fff" stroke-width="1"/>
        </svg>
      </li>
      <li class="contact-item">
        <span>www.pixelharbor.example</span>
        <svg class="contact-icon" viewBox="0 0 14 14" aria-hidden="true">
          <rect width="14" height="14" fill="var(--brand-green)"/>
          <rect x="3" y="3.5" width="8" height="5.5" fill="none" stroke="#fff" stroke-width="1"/>
          <path d="M5 11 H9" stroke="#fff" stroke-width="1"/>
        </svg>
      </li>
    </ul>
  </section>
</main>
</body>
</html>
```